Web site design for volunteer-travel agency

Hi there,
Thanks for drew attention to this project :) The main idea of this website inspire people to travel and see the world.
About the project:
it calls Roam 9 Lite. We are ceating new kind of travel agency, the main idea that you can travel using volunteers programs. it is not tipical volunteer programs, the main idea you work somethere 20 hours at week for food and accomodation. For example on reception in a hostel or you help on a farm or with eco project or babysiting. You can see this type of project here: fernhollow.info, bryxal.net. Our agency will help choose the program, agree on the details on a trip, submit requests. So, we work like a travel agency for this kind of travels. Our cliens young active people, that want to learn language, travel and explore new culture.
About website:
- Firts of all it should inspire, first look at a first page and you want travel :) I think following websites give the right expresion: http://www.quindlevoyage.com/, http://www.molvaneta.ru/, http://www.pzelk.net/, http://www.dovrimo.com/.
- It should be very simple and understandeble
- i will explain website on structure we need main page (impresive picture that associated with travelling, young people, fun, volunteering, hot offers, inspiring sentence, social network signes, log in/registration), page with travel offers (just example so you can get better: http://www.dovrimo.com/ru/special_offers/activities/1-skiing), offer page (example^ http://www.dovrimo.com/ru/special_offers/367-lyzhnyy-tur-na-vyhodnyh-v-bakuriani (better if you do you own style)), registration page, log in window, private office pages (sorry not sure it is a right name in English, hope you understand). The website will work like a on-line shop, you choose right travel programs, put it in your shopping bag, fill aplication form, pay agency fee.
Hope i explained main idea, please dont hesitate ask me more questions.
Target Market(s)
Young people, 18-30
Industry/Entity Type
Shopping

```html
<!DOCTYPE html>
<html lang="en">
<head>
<meta charset="utf-8">
<title>Roam 9 Lite</title>
<link rel="stylesheet" href="https://fonts.googleapis.com/css2?family=Source+Sans+3:wght@400;600;700&family=Arimo:wght@400;700&display=swap">
<style>
:root{
  --page:#f3f3f3;
  --ink:#333333;
  --dark:#2f2f2f;
  --blue:#3a87cf;
  --link:#59a8f0;
  --green:#8bbd23;
  --orange:#f0a030;
  --purple:#b23bbf;
  --teal:#2fb6c8;
  --line:#d8d8d8;
  --white:#ffffff;
}
*{margin:0;padding:0;box-sizing:border-box}
html,body{width:1080px;height:1200px;overflow:hidden;background:var(--page)}
body{font-family:"Arimo",Arial,sans-serif;color:var(--ink)}
.page{position:absolute;left:0;top:0;width:1237px;height:1375px;transform:scale(0.8731);transform-origin:0 0;background:var(--page)}
.abs{position:absolute}
.head{font-family:"Source Sans 3",sans-serif;font-weight:700}

.brand-mark{left:150px;top:36px;width:90px;height:90px;border-radius:50%;background:var(--blue)}
.brand-name{left:285px;top:48px;font-size:52px;color:var(--blue);letter-spacing:-1px;line-height:1}

.search-field{left:851px;top:46px;width:218px;height:28px;background:var(--white);border:1px solid var(--line)}
.search-btn{left:1069px;top:46px;width:29px;height:28px;background:var(--dark)}
.util-btn{top:85px;width:78px;height:28px;background:var(--white);border:1px solid var(--line);font-size:13px;text-align:center;line-height:26px;color:var(--ink)}

.nav a{position:absolute;top:160px;height:57px;color:var(--white);font-family:"Source Sans 3",sans-serif;font-weight:700;font-size:25px;text-decoration:none;text-align:center;line-height:57px}
.nav-rule{left:138px;top:217px;width:960px;height:5px;background:var(--dark)}

.tab{top:258px;width:66px;height:31px;background:var(--blue);color:var(--white);font-size:12px;font-weight:700;text-align:center;line-height:31px;font-family:"Source Sans 3",sans-serif}
.tab.active{background:var(--dark)}
.booking{left:138px;top:289px;width:267px;height:322px;background:var(--dark);color:var(--white);font-size:13.5px}
.booking .abs{white-space:nowrap}
.radio{display:inline-block;width:10px;height:10px;border-radius:50%;background:#ccc;border:2px solid #999;margin-right:6px;vertical-align:-1px}
.radio.on{background:var(--blue);border-color:#ddd}
.input{background:var(--white);height:18px}
.date{background:var(--white);color:#666;font-size:11px;padding-left:8px;line-height:18px;width:78px;height:18px}
.link{color:var(--link);text-decoration:underline}
.go-btn{background:var(--blue);color:var(--white);font-size:11px;font-weight:700;text-align:center;line-height:25px;width:66px;height:25px;border-radius:2px}

.hero-photo{left:715px;top:235px;width:395px;height:415px;border-radius:40% 40% 10% 10%;background:radial-gradient(circle at 60% 40%,#3e5f94 0%,#2e4570 45%,#e9ebee 75%)}
.offer-num{left:448px;top:301px;background:var(--green);color:var(--white);font-size:46px;padding:0 6px;line-height:46px;letter-spacing:-2px}
.offer-word{left:565px;top:292px;color:var(--green);font-size:60px;letter-spacing:-3px;line-height:60px}
.offer-sub{left:467px;top:352px;font-size:30px;color:var(--ink);letter-spacing:-0.5px}
.offer-text{left:447px;top:407px;width:272px;font-size:12px;font-weight:700;line-height:20px}
.read-more{left:523px;top:512px;width:115px;height:33px;background:var(--orange);color:var(--white);font-size:15px;text-align:center;line-height:33px}

.hot-bar{left:138px;top:647px;width:267px;height:56px;background:var(--blue);color:var(--white);font-size:26px;line-height:56px;padding-left:36px}
.thumb{left:151px;width:116px;height:116px}
.hot-title{left:285px;font-size:13.5px;font-weight:700;line-height:17px}
.hot-text{left:285px;font-size:12.5px;line-height:17px;width:105px}
.dot{width:17px;height:17px}
.sep{height:1px;background:var(--line)}

.places-title{left:448px;top:652px;font-size:39px;color:var(--blue)}
.place-img{left:447px;width:246px;height:194px}
.place-title{left:711px;font-size:13.5px;font-weight:700}
.place-text{left:711px;width:388px;font-size:12.5px;line-height:17px}
.place-text p{margin-bottom:7px}

.footer{left:0;top:1275px;width:1237px;height:100px;background:var(--dark)}
.credit{left:0;top:1306px;width:1237px;text-align:center;color:var(--white);font-size:13px}
.credit span{color:var(--link);text-decoration:underline}
</style>
</head>
<body>
<div class="page">

  <div class="abs brand-mark"></div>
  <div class="abs head brand-name">Roam 9 Lite</div>

  <div class="abs search-field"></div>
  <div class="abs search-btn">
    <svg width="29" height="28" viewBox="0 0 29 28"><circle cx="13" cy="12" r="6" fill="none" stroke="#fff" stroke-width="2.5"/><line x1="17.5" y1="16.5" x2="22" y2="21" stroke="#fff" stroke-width="3"/></svg>
  </div>
  <div class="abs util-btn" style="left:851px">Register</div>
  <div class="abs util-btn" style="left:935px">Log In</div>
  <div class="abs util-btn" style="left:1019px">Help</div>

  <nav class="nav">
    <a style="left:138px;width:140px;background:var(--blue)">HOME</a>
    <a style="left:280px;width:185px;background:var(--green)">ABOUT US</a>
    <a style="left:467px;width:201px;background:var(--orange)">OUR TOURS</a>
    <a style="left:670px;width:235px;background:var(--purple)">DESTINATIONS</a>
    <a style="left:907px;width:191px;background:var(--teal)">CONTACTS</a>
  </nav>
  <div class="abs nav-rule"></div>

  <div class="abs tab active" style="left:138px">HOSTEL</div>
  <div class="abs tab" style="left:205px">FARM</div>
  <div class="abs tab" style="left:272px">ECO</div>
  <div class="abs tab" style="left:339px">FAMILY</div>
  <form class="abs booking">
    <div class="abs" style="left:35px;top:33px"><span class="radio on"></span>Short stay</div>
    <div class="abs" style="left:128px;top:33px"><span class="radio"></span>Long stay</div>
    <div class="abs link" style="left:35px;top:58px">Multiple destinations</div>
    <div class="abs" style="left:35px;top:82px">From</div>
    <div class="abs input" style="left:83px;top:81px;width:149px"></div>
    <div class="abs" style="left:35px;top:106px">To</div>
    <div class="abs input" style="left:83px;top:105px;width:149px"></div>
    <div class="abs" style="left:40px;top:141px"><span style="display:inline-block;width:11px;height:11px;background:#fff;color:#333;font-size:10px;line-height:11px;text-align:center;margin-right:4px">✓</span><span class="link">Search nearby hosts</span></div>
    <div class="abs" style="left:35px;top:166px">Start (mm/dd/yy)</div>
    <div class="abs date" style="left:154px;top:165px">04/11/2010</div>
    <div class="abs" style="left:35px;top:190px">End (mm/dd/yy)</div>
    <div class="abs date" style="left:154px;top:189px">04/11/2010</div>
    <div class="abs" style="left:35px;top:231px"><span class="radio on"></span>20 hours/week</div>
    <div class="abs" style="left:156px;top:231px"><span class="radio"></span>Full time</div>
    <div class="abs" style="left:35px;top:258px">People</div>
    <div class="abs input" style="left:80px;top:256px;width:58px;color:#333;padding-left:6px;line-height:18px">1<span style="position:absolute;right:2px;top:2px;width:13px;height:13px;border:1px solid #999;font-size:8px;text-align:center;line-height:12px">▼</span></div>
    <div class="abs go-btn" style="left:166px;top:251px">SEARCH</div>
  </form>

  <div class="abs hero-photo" role="img" aria-label="Travel suitcase on wheels beside a desk globe and folded maps"></div>
  <div class="abs head offer-num">5000</div>
  <div class="abs head offer-word">hosts</div>
  <div class="abs head offer-sub">THE BEST OFFERS</div>
  <p class="abs offer-text">Work 20 hours a week for food and a bed, learn a language and explore new cultures with hosts all over the world.</p>
  <div class="abs head read-more">READ MORE</div>

  <div class="abs head hot-bar">HOT TRAVEL</div>

  <div class="abs thumb" style="top:734px;background:linear-gradient(#6aa6dd 0%,#9cc4e6 35%,#b08a5a 40%,#6d5436 100%)" role="img" aria-label="Ancient amphitheatre ruins in Italy"></div>
  <div class="abs hot-title" style="top:734px">Italy<br>Farm Stays</div>
  <div class="abs hot-text" style="top:775px">Pick olives, cook with locals and learn Italian.</div>
  <svg class="abs dot" style="left:151px;top:850px" viewBox="0 0 17 17"><circle cx="8.5" cy="8.5" r="8.5" fill="#8bbd23"/><path d="M7 5l4 3.5L7 12" fill="none" stroke="#fff" stroke-width="2"/></svg>
  <div class="abs sep" style="left:151px;top:887px;width:241px"></div>

  <div class="abs thumb" style="top:908px;background:linear-gradient(#5fa2d8 0%,#bde0f0 40%,#4fc4c0 55%,#a8ddc8 100%)" role="img" aria-label="Thatched beach umbrella in clear tropical water"></div>
  <div class="abs hot-title" style="top:908px">Philippines<br>Eco Work</div>
  <div class="abs hot-text" style="top:949px">Help a reef project and live by the sea.</div>
  <svg class="abs dot" style="left:151px;top:1024px" viewBox="0 0 17 17"><circle cx="8.5" cy="8.5" r="8.5" fill="#8bbd23"/><path d="M7 5l4 3.5L7 12" fill="none" stroke="#fff" stroke-width="2"/></svg>
  <div class="abs sep" style="left:151px;top:1061px;width:241px"></div>

  <div class="abs thumb" style="top:1082px;background:linear-gradient(135deg,#2e7fd0 0%,#6cb0e8 45%,#3f8f3a 60%,#e6d2a0 100%)" role="img" aria-label="Palm tree over a beach with a cruise ship offshore"></div>
  <div class="abs hot-title" style="top:1081px">Island<br>Hostel Work</div>
  <div class="abs hot-text" style="top:1122px">Run a beach hostel desk, surf after shifts.</div>
  <svg class="abs dot" style="left:151px;top:1198px" viewBox="0 0 17 17"><circle cx="8.5" cy="8.5" r="8.5" fill="#8bbd23"/><path d="M7 5l4 3.5L7 12" fill="none" stroke="#fff" stroke-width="2"/></svg>

  <h2 class="abs head places-title">POPULAR PLACES</h2>

  <div class="abs place-img" style="top:734px;background:linear-gradient(#4aa0e8 0%,#e9e3d6 35%,#c9c1b0 65%,#4d8a3a 85%,#2f6a2a 100%)" role="img" aria-label="Historic seaside guesthouse with flower gardens in front"></div>
  <div class="abs place-title" style="top:734px">Hostel Merivale</div>
  <div class="abs place-text" style="top:758px">
    <p>Work on the reception desk of a busy seaside hostel for twenty hours a week. In return you get a free bed in a shared room, breakfast every day and plenty of time to explore the coast.</p>
    <p><b>Who we are looking for:</b> friendly people who enjoy meeting travellers, speak some English and want to practise French. You will welcome guests, help with check-in and share tips about the town.</p>
  </div>
  <svg class="abs dot" style="left:711px;top:908px" viewBox="0 0 17 17"><circle cx="8.5" cy="8.5" r="8.5" fill="#f0a030"/><path d="M7 5l4 3.5L7 12" fill="none" stroke="#fff" stroke-width="2"/></svg>
  <div class="abs sep" style="left:447px;top:949px;width:650px"></div>

  <div class="abs place-img" style="top:970px;background:linear-gradient(#7fb2e0 0%,#d8dee6 30%,#c98a7a 55%,#3f8a3a 80%,#8fd0e0 100%)" role="img" aria-label="Tall resort building with palm trees and a pool"></div>
  <div class="abs place-title" style="top:970px">Eco Farm Solvanne</div>
  <div class="abs place-text" style="top:994px">
    <p>Join a small organic farm near the coast and help with planting, harvest and caring for the animals. Hosts share home-cooked meals, a private room and weekend trips to nearby villages.</p>
    <p>Perfect for young travellers who want to slow down, learn how food is grown and pick up the local language. Stays last from two weeks to three months, and our team handles every detail.</p>
  </div>
  <svg class="abs dot" style="left:711px;top:1144px" viewBox="0 0 17 17"><circle cx="8.5" cy="8.5" r="8.5" fill="#f0a030"/><path d="M7 5l4 3.5L7 12" fill="none" stroke="#fff" stroke-width="2"/></svg>

  <footer class="abs footer"></footer>
  <p class="abs credit">Website template designed by <span>Brindlecove Studio Pvt. Ltd.</span></p>
</div>
</body>
</html>
```